Design our branded business card!

We'd love for you to design our business card and come up with a fitting design that reflects the Pivex brand. We're a growing tech startup with big ambitions. We've included our brand guidelines (contain colour palette), logo (EPS vector in CMYK) and old designs to help you on your way.

We'd like to keep the design fairly simple:

* Name
* Phone number
* Email address
* Website (www.pivex.life)
* Twitter (@pivex)
* Address (18 Wexham Row, Leeds, UK, LS9 4ZQ).

This would need to include print and cutting marks.

If you have any questions just let us know!

Target Market(s)

Businesses, Press and our customers!

Industry/Entity Type

Business

Contact Information for Business Card

* Name
* Phone number
* Email address
* Twitter (@pivex)

Font styles to use
Sans Serif

Requirements
Must have
• 1. Must have the Pivex logo included.
• 2. Must use the font 'Brandon Text' in either 'light' or 'thin' (https://www.typevault-demo.com/fonts/qrsfonts/halden-sans/)
• 3. Must use exact colours references from the brand guidelines. Colours outside of the brand guidelines will be discounted. White (transparent) backgrounds are fine.
• 4. Must contain the following information:
• * Name
• * Phone number
• * Email address
• * Website (www.pivex.life)
• * Twitter (@pivex)
• * Address (18 Wexham Row, Leeds, UK, LS9 4ZQ).
Nice to have
• Must use the font 'Brandon Text' in either 'light' or 'thin' (https://www.typevault-demo.com/fonts/qrsfonts/halden-sans/)
Should not have
• Colours outside of the brand guidelines will be discounted. White (transparent) backgrounds are fine.
• Avoid creating icons or including photography.

```html
<!DOCTYPE html>
<html lang="en">
<head>
<meta charset="utf-8">
<title>Pivex Business Card</title>
<link rel="stylesheet" href="https://fonts.googleapis.com/css2?family=Josefin+Sans:wght@400&family=Open+Sans:wght@400;600&display=swap">
<style>
  :root {
    --brand-green: #7dc273;
    --ink-dark: #343c3a;
    --ink-body: #3a3a3a;
    --card-white: #ffffff;
    --backdrop: #e9ebe8;
  }
  * { margin: 0; padding: 0; box-sizing: border-box; }
  html, body { width: 1200px; height: 900px; overflow: hidden; }
  body {
    position: relative;
    background: var(--backdrop);
    font-family: "Open Sans", Arial, sans-serif;
  }
  .card {
    position: absolute;
    border-radius: 16px;
    overflow: hidden;
    box-shadow: 0 6px 20px rgba(0,0,0,0.15);
  }
  .card--front {
    left: 78px; top: 35px; width: 587px; height: 363px;
    background: var(--card-white);
  }
  .card--back {
    left: 390px; top: 506px; width: 565px; height: 350px;
    background: var(--brand-green);
  }
  .band { position: absolute; left: 0; width: 100%; }
  .card--front .band { top: 31px; height: 98px; background: var(--brand-green); }
  .card--back .band { top: 97px; height: 97px; background: var(--card-white); }
  .brand-disc {
    position: absolute;
    width: 140px; height: 140px;
    border-radius: 50%;
    background: var(--brand-green);
    border: 7px solid var(--card-white);
  }
  .card--front .brand-disc { left: 223px; top: 10px; }
  .card--back .brand-disc { left: 212px; top: 78px; }
  .wordmark {
    position: absolute;
    left: 0; width: 100%;
    text-align: center;
    font-family: "Josefin Sans", "Open Sans", sans-serif;
    font-weight: 400;
    font-size: 84px;
    line-height: 1;
    letter-spacing: 2px;
  }
  .card--front .wordmark { top: 140px; color: var(--ink-dark); }
  .card--back .wordmark { top: 205px; color: var(--card-white); }
  .holder {
    position: absolute; left: 22px; top: 258px;
  }
  .holder__name {
    color: var(--brand-green);
    font-weight: 600;
    font-size: 21px;
    line-height: 28px;
  }
  .holder__address {
    margin-top: 6px;
    color: var(--ink-body);
    font-size: 15px;
  }
  .contacts {
    position: absolute;
    right: 36px; top: 236px;
    list-style: none;
  }
  .contacts li {
    display: flex; align-items: center; justify-content: flex-end;
    height: 24.5px;
    color: var(--ink-body);
    font-size: 15px;
  }
  .contacts svg { width: 12px; height: 12px; margin-left: 9px; fill: var(--brand-green); }
</style>
</head>
<body>
  <section class="card card--front" aria-label="Card front">
    <div class="band"></div>
    <div class="brand-disc"></div>
    <div class="wordmark">pivex</div>
    <div class="holder">
      <p class="holder__name">Marcus Hale</p>
      <p class="holder__address">18 Wexham Row, Leeds,&nbsp; UK, LS9 4ZQ</p>
    </div>
    <ul class="contacts">
      <li>(044)-318-2265
        <svg viewBox="0 0 12 12"><path d="M2.5 1 L4.5 1 L5.3 3.6 L4 4.6 Q5 7 7.4 8 L8.4 6.7 L11 7.5 L11 9.5 Q10.5 11 9 11 Q1 10 1 3 Q1 1.5 2.5 1Z"/></svg></li>
      <li>info@pivexmail.com
        <svg viewBox="0 0 12 12"><path d="M0.5 2 H11.5 V10 H0.5Z M1.5 3 L6 6.6 L10.5 3" fill="var(--brand-green)" stroke="#fff" stroke-width="1"/></svg></li>
      <li>www.pivex.life
        <svg viewBox="0 0 12 12" fill="none"><path d="M5 7 L7 5 M4.5 5.5 L2.5 7.5 A2 2 0 0 0 4.5 9.5 L6.5 7.5 M7.5 6.5 L9.5 4.5 A2 2 0 0 0 7.5 2.5 L5.5 4.5" stroke="var(--brand-green)" stroke-width="1.4" fill="none"/></svg></li>
      <li>@pivex
        <svg viewBox="0 0 12 12"><circle cx="6" cy="6" r="5"/></svg></li>
    </ul>
  </section>

  <section class="card card--back" aria-label="Card back">
    <div class="band"></div>
    <div class="brand-disc"></div>
    <div class="wordmark">pivex</div>
  </section>
</body>
</html>
```